Frizzle! A stand up comedy show- poster and other graphics required

We require a design for a new late night comedy show called 'Frizzle!' which will appear at festivals and feature a variety of stand up acts as well as inviting the audience to heckle the comedians on stage. The final design should be bold and stand out loudly, to fit the late night raucous nature of the show.
We need a poster image as well as smaller images for program guides and websites. This is going to be the kind of show people talk about so needs a poster to match!!

Target Market(s)

Comedy fans, 20-40 year olds, late night adult audience

Requirements
Nice to have
• We don't really have any clear design in mind so happy to leave it to interpretation but possible ideas would be: a silhouette of a head shouting / a mic is always an iconic image / the simple outline of an audience with obscenities (@*!& etc) coming out of them / perhaps a mic having fallen over because of a stand-up running off stage!
• But again these are vague ideas. Please message for more info about the show if it helps
Should not have
• Not too busy

```html
<!DOCTYPE html>
<html lang="en">
<head>
<meta charset="utf-8">
<title>Frizzle! – Night Comedy Show</title>
<link rel="stylesheet" href="https://fonts.googleapis.com/css2?family=Titan+One&family=Kalam:wght@400;700&display=swap">
<style>
  :root {
    --sky-deep: #050a2e;
    --sky-mid: #13207a;
    --sky-light: #2c3cb0;
    --haze: #3b4a9e;
    --cream: #fbf6cf;
    --cream-shadow: #c9bf7a;
    --ink: #0b0f2a;
    --star: #ffffff;
    --star-glow: rgba(255, 255, 240, 0.85);
  }
  * { margin: 0; padding: 0; box-sizing: border-box; }
  html, body {
    width: 900px;
    height: 1200px;
    overflow: hidden;
    background: var(--sky-deep);
  }
  .poster {
    position: relative;
    width: 900px;
    height: 1200px;
    overflow: hidden;
    background:
      radial-gradient(ellipse 380px 260px at 200px 260px, rgba(59, 74, 158, 0.55), transparent 70%),
      radial-gradient(ellipse 420px 300px at 700px 500px, rgba(44, 60, 176, 0.6), transparent 70%),
      radial-gradient(ellipse 360px 280px at 250px 820px, rgba(59, 74, 158, 0.5), transparent 70%),
      radial-gradient(ellipse 400px 260px at 680px 1050px, rgba(44, 60, 176, 0.5), transparent 70%),
      radial-gradient(ellipse 300px 200px at 480px 120px, rgba(30, 44, 150, 0.6), transparent 70%),
      linear-gradient(160deg, var(--sky-mid) 0%, var(--sky-deep) 40%, var(--sky-mid) 70%, var(--sky-deep) 100%);
  }
  .starfield {
    position: absolute;
    inset: 0;
    width: 900px;
    height: 1200px;
  }
  .mascot-glow {
    position: absolute;
    left: 320px;
    top: 90px;
    width: 240px;
    height: 240px;
    border-radius: 50%;
    background: radial-gradient(circle, rgba(251, 246, 207, 0.55) 0%, rgba(201, 191, 122, 0.25) 45%, transparent 72%);
  }
  .show-title {
    position: absolute;
    left: 0;
    top: 470px;
    width: 900px;
    text-align: center;
    font-family: "Titan One", "Arial Black", sans-serif;
    font-size: 124px;
    letter-spacing: 4px;
    color: var(--cream);
    -webkit-text-stroke: 5px var(--ink);
    paint-order: stroke fill;
    text-shadow: 6px 8px 0 var(--ink), 0 0 18px rgba(251, 246, 207, 0.35);
    transform: rotate(-7deg) skewX(-6deg);
  }
  .title-swoosh {
    position: absolute;
    left: 270px;
    top: 600px;
    width: 460px;
    height: 90px;
  }
  .tagline {
    position: absolute;
    font-family: "Kalam", cursive;
    font-style: italic;
    color: var(--cream);
    text-decoration: line-through;
    text-decoration-thickness: 3px;
    text-shadow: 3px 3px 0 var(--ink);
  }
  .tagline-stage {
    left: 612px;
    top: 820px;
    font-size: 40px;
    font-variant: small-caps;
    font-weight: 400;
  }
  .tagline-show {
    left: 292px;
    top: 868px;
    font-size: 68px;
    font-weight: 400;
    letter-spacing: 1px;
  }
</style>
</head>
<body>
  <main class="poster">
    <svg class="starfield" viewBox="0 0 900 1200" aria-hidden="true">
      <defs>
        <filter id="star-glow" x="-200%" y="-200%" width="500%" height="500%">
          <feGaussianBlur stdDeviation="6" result="blur"/>
          <feMerge>
            <feMergeNode in="blur"/>
            <feMergeNode in="blur"/>
            <feMergeNode in="SourceGraphic"/>
          </feMerge>
        </filter>
        <polygon id="star" points="0,-16 4.7,-5 16,-5 7,2 10.5,14 0,7 -10.5,14 -7,2 -16,-5 -4.7,-5" fill="var(--star)"/>
      </defs>
      <g filter="url(#star-glow)">
        <use href="#star" transform="translate(96 66)"/>
        <use href="#star" transform="translate(210 174)"/>
        <use href="#star" transform="translate(666 126)"/>
        <use href="#star" transform="translate(729 84)"/>
        <use href="#star" transform="translate(795 54)"/>
        <use href="#star" transform="translate(555 285)"/>
        <use href="#star" transform="translate(840 180)"/>
        <use href="#star" transform="translate(36 591)"/>
        <use href="#star" transform="translate(744 525)"/>
        <use href="#star" transform="translate(264 870)"/>
        <use href="#star" transform="translate(318 1038)"/>
        <use href="#star" transform="translate(786 1059)"/>
      </g>
    </svg>

    <div class="mascot-glow" role="img" aria-label="Glowing cream smiling-moon mascot floating in the night sky"></div>

    <h1 class="show-title">FRIZZLE</h1>

    <svg class="title-swoosh" viewBox="0 0 460 90" aria-hidden="true">
      <path d="M10 70 Q 220 40 450 8" fill="none" stroke="var(--ink)" stroke-width="14" stroke-linecap="round"/>
      <path d="M10 66 Q 220 36 450 4" fill="none" stroke="var(--cream)" stroke-width="7" stroke-linecap="round"/>
    </svg>

    <p class="tagline tagline-stage">On Stage</p>
    <p class="tagline tagline-show">Night Comedy Show</p>
  </main>
</body>
</html>
```